Copperleaf Motorized Shade Business Card

Hello, we've had our logo made. Now we are looking for a clean and cool looking business card. One side can just be the logo with any design elements that might look good with it. The other side will be Name, Phone Number and Email. There will not be an address on the card.

```html
<!DOCTYPE html>
<html lang="en">
<head>
<meta charset="utf-8">
<title>Copperleaf Motorized Shade – Business Card</title>
<link rel="stylesheet" href="https://fonts.googleapis.com/css2?family=Bebas+Neue&family=Montserrat:wght@600&family=Poppins:wght@500&display=swap">
<style>
  :root {
    --navy: #0e3a73;
    --sky: #00adef;
    --gold: #fec20f;
    --cream: #fdf7e6;
    --paper: #ffffff;
  }
  html, body {
    margin: 0;
    padding: 0;
    width: 1090px;
    height: 1200px;
    overflow: hidden;
    background: var(--paper);
  }
  .canvas {
    position: relative;
    width: 1090px;
    height: 1200px;
  }
  .backdrop {
    position: absolute;
    left: 0; top: 0;
    width: 1033px;
    height: 1192px;
    background: var(--cream);
  }
  .card {
    position: absolute;
    left: 40px;
    width: 953px;
    height: 545px;
    filter: drop-shadow(3px 3px 5px rgba(60, 45, 30, 0.55));
  }
  .card svg { display: block; width: 953px; height: 545px; }
  .card--front { top: 33px; }
  .card--back { top: 615px; }

  .brand-name {
    font-family: "Bebas Neue", sans-serif;
    fill: var(--navy);
  }
  .person-name {
    font-family: "Bebas Neue", sans-serif;
    font-size: 100px;
    fill: var(--navy);
    letter-spacing: 1px;
  }
  .person-role {
    font-family: "Montserrat", sans-serif;
    font-weight: 600;
    font-size: 33px;
    letter-spacing: 6px;
    fill: var(--navy);
  }
  .contact-text {
    font-family: "Poppins", sans-serif;
    font-weight: 500;
    font-size: 26px;
    letter-spacing: 2.5px;
    fill: var(--navy);
  }
</style>
</head>
<body>
<main class="canvas">
  <div class="backdrop"></div>

  <section class="card card--front" aria-label="Card front">
    <svg viewBox="0 0 1050 600" xmlns="http://www.w3.org/2000/svg">
      <rect class="front-field" width="1050" height="600" fill="var(--navy)"/>
      <circle class="ring-outer" cx="525" cy="300" r="268" fill="var(--sky)"/>
      <circle class="ring-inner" cx="525" cy="300" r="250" fill="var(--gold)"/>
      <circle class="logo-disc" cx="525" cy="300" r="233" fill="var(--cream)"/>
      <text class="brand-name" x="525" y="340" text-anchor="middle" font-size="104">COPPERLEAF</text>
      <text class="brand-name" x="525" y="395" text-anchor="middle" font-size="34" letter-spacing="7">MOTORIZED SHADE</text>
    </svg>
  </section>

  <section class="card card--back" aria-label="Card back">
    <svg viewBox="0 0 1050 600" xmlns="http://www.w3.org/2000/svg">
      <rect class="back-field" width="1050" height="600" fill="var(--cream)"/>
      <polygon class="corner-stripe" points="474,0 487,0 425,168 411,168" fill="var(--gold)"/>
      <polygon class="corner-band" points="0,0 474,0 411,168 0,168" fill="var(--navy)"/>
      <rect class="divider" x="0" y="298" width="1050" height="9" fill="var(--gold)"/>
      <polygon class="corner-stripe" points="563,433 576,433 639,600 626,600" fill="var(--gold)"/>
      <polygon class="corner-band" points="576,433 1050,433 1050,600 639,600" fill="var(--navy)"/>

      <text class="person-name" x="986" y="278" text-anchor="end">DANIEL REYES</text>
      <text class="person-role" x="786" y="349" text-anchor="middle">MANAGER</text>

      <g class="contact contact--phone">
        <circle cx="57" cy="487" r="20" fill="var(--navy)"/>
        <path d="M49.5 477.5c1.5-1 3-.5 3.8 1l1.7 3c.6 1.1.3 2.3-.7 3l-1 .8c.9 2.3 2.7 4.3 5 5.4l.9-1c.8-.9 2-1.1 3-.5l3 1.8c1.4.8 1.8 2.4.8 3.7-1.5 2-3.7 2.8-6 2-5.8-2-10.3-6.6-12.2-12.5-.7-2.5.1-4.8 1.7-6.7z" fill="var(--gold)"/>
        <text class="contact-text" x="104" y="496">+1-555-014-27</text>
      </g>
      <g class="contact contact--email">
        <circle cx="57" cy="551" r="20" fill="var(--navy)"/>
        <rect x="45.5" y="543" width="23" height="16" rx="1.5" fill="none" stroke="var(--gold)" stroke-width="2.5"/>
        <path d="M46.5 544.5l10.5 8 10.5-8" fill="none" stroke="var(--gold)" stroke-width="2.5"/>
        <text class="contact-text" x="106" y="560">daniel.reyes@mail.com</text>
      </g>
    </svg>
  </section>
</main>
</body>
</html>
```